Webdesign für Kleingruppenreisen in die Südsteiermark
Zielgruppe
Wir sind ein Start-Up Unternehmen, das als Kleingruppenreisen in die Südsteiermark veranstaltet; der Schwerpunkt liegt auf dem Kulinarischen. Zielgruppe sind Geschäftsleute, die diese Kurzreisen (Do-So) für Marketingzwecke oder als Mitarbeiterbonus (oder auch privat) nutzen möchten.
Aufgabenstellung
Die Homepage soll eine Online-Shop Möglichkeit bieten, in der die Reise (bisher gibt es nur einen Ablauf) gebucht werden kann. Optisch sollte sie sich an das bereits von Ihnen erstellte Logo anlehnen und möglichst ansprechende Fotos von der Südsteiermark, Graz, Leoben usw. enthalten. (Siehe die beiden Flyer und das Logo)
Wir haben inzwischen Bildfreigaben von Mirtler und dem Tourismusverband Hollerau erhalten und können auch eigene Bilder zur Verfügung stellen. Bitte kontaktieren Sie uns dafür, wenn nötig.

```html
<!DOCTYPE html>
<html lang="de">
<head>
<meta charset="utf-8">
<title>Gaumenweg Reisen – Produktseite</title>
<link href="https://fonts.googleapis.com/css2?family=Open+Sans:ital,wght@0,300;0,400;0,600;0,700;1,400;1,600;1,700&family=Kaushan+Script&family=PT+Sans+Narrow&display=swap" rel="stylesheet">
<style>
:root{
  --green:#236340;
  --green-dark:#1b4f33;
  --text:#2b2b2b;
  --muted:#6e6e6e;
  --field:#ececec;
  --btn:#6d6d6d;
  --dot:#c4c4c4;
  --white:#fff;
}
*{box-sizing:border-box;margin:0;padding:0}
html,body{width:797px;height:1200px;overflow:hidden;background:var(--white)}
body{position:relative;font-family:"Open Sans",sans-serif;color:var(--text)}
.abs{position:absolute}
.topbar{left:0;top:0;width:797px;height:25px;background:var(--green)}
.brand{left:70px;top:55px;display:flex;align-items:center;gap:7px;font-size:17px;font-weight:600;color:var(--green)}
.brand-dot{width:14px;height:14px;border-radius:50%;background:var(--green)}
.nav{top:61px;left:306px;display:flex;gap:13px;font-size:11px;color:#6a6a6a}
.nav a{color:inherit;text-decoration:none}
.nav .active{color:var(--green);font-weight:600}
.search{left:627px;top:61px}
.hero{left:0;top:120px;width:797px;height:135px;background:linear-gradient(90deg,#6f8a62 0%,#8a9a86 30%,#9a7b62 55%,#5f7c3e 75%,#4c6e2e 100%)}
.hero-title{left:71px;top:157px;font-family:"Kaushan Script",cursive;font-size:23px;color:var(--white)}
.hero-sub{left:71px;top:184px;font-family:"PT Sans Narrow",sans-serif;font-size:20px;color:var(--white)}
.feature{left:71px;top:325px;width:249px;height:249px;background:linear-gradient(170deg,#7e9a4d 0%,#9aa86a 35%,#6b5a3e 65%,#5e4a33 100%)}
.feature-script{right:6px;top:148px;font-family:"Kaushan Script",cursive;font-size:16px;color:var(--white)}
.feature-text{right:6px;top:167px;font-size:9px;font-weight:700;color:var(--white);text-align:right;line-height:12px}
.feature-btn{left:156px;top:203px;width:83px;height:21px;background:rgba(255,255,255,.8);font-size:10px;font-style:italic;text-align:center;line-height:21px;color:#111}
.thumb{top:325px;width:116px;height:116px}
.t1{left:361px;background:linear-gradient(160deg,#d9e2e4 0%,#6e9440 45%,#3f6a24 100%)}
.t2{left:485px;background:linear-gradient(170deg,#7fb0de 0%,#d98a4c 40%,#b5563b 75%,#5d6470 100%)}
.t3{left:610px;background:linear-gradient(180deg,#5f99d4 0%,#8aa08e 35%,#3d8fa6 60%,#c9d3d1 100%)}
.dots{top:453px;left:361px;width:366px;height:10px}
.dot{position:absolute;top:2px;width:6px;height:6px;border-radius:50%;background:var(--dot)}
.dot.on{background:#111}
.price{left:361px;top:470px;font-size:21px;font-weight:300;color:var(--green);letter-spacing:-.5px}
.vat{left:361px;top:492px;font-size:5px;color:var(--muted)}
.wish{left:486px;top:477px;display:flex;align-items:center;gap:5px;font-size:8px;color:#333}
.field{top:511px;width:116px;height:21px;background:var(--field);font-size:7px;font-style:italic;color:#9a9a9a;padding:0 6px;display:flex;align-items:center;justify-content:space-between}
.book{left:361px;top:545px;width:116px;height:29px;background:var(--btn);color:var(--white);font-size:10.5px;font-style:italic;font-weight:600;text-align:center;line-height:29px}
.intro-title{left:71px;top:615px;font-family:"Kaushan Script",cursive;font-size:16px;color:#555}
.intro{left:71px;top:651px;width:660px;font-size:7.2px;line-height:8.9px;color:#222}
.intro p+p{margin-top:9px}
.banner{left:0;top:757px;width:797px;height:194px;background:linear-gradient(110deg,#4e7340 0%,#5b6f7d 35%,#4f6570 55%,#6b8a4a 80%,#86a65a 100%)}
.banner-title{left:151px;top:782px;font-size:19px;line-height:24px;font-style:italic;font-weight:700;color:var(--white)}
.banner-sub{left:151px;top:855px;font-size:15px;line-height:17.5px;font-weight:300;color:var(--white)}
.banner-btn{left:459px;top:884px;width:191px;height:29px;border:1px solid var(--white);color:var(--white);font-size:15px;font-style:italic;font-weight:600;text-align:center;line-height:27px}
.hills{left:0;top:980px;width:366px;height:84px;background:linear-gradient(180deg,rgba(35,99,64,0) 0%,rgba(35,99,64,.55) 55%,var(--green) 100%)}
.footer{left:0;top:1064px;width:797px;height:134px;background:var(--green);color:var(--white);font-size:7.6px;line-height:9px}
.footer-bottom{left:0;top:1197px;width:797px;height:3px;background:#111}
.f-name{left:166px;top:1085px;font-size:9px;font-weight:600;color:var(--white)}
.f-addr{left:166px;top:1097px;color:var(--white);font-size:7.6px;line-height:9px}
.f-phone{left:166px;top:1133px;color:var(--white);font-size:7.6px;line-height:9px}
.f-ico{color:var(--white)}
.f-col{top:1087px;color:var(--white);font-size:7.4px}
.f-col h4{font-size:7.4px;font-weight:700;margin-bottom:6px}
.f-col li{list-style:none;margin-bottom:5.5px}
.f-rule{left:150px;top:1167px;width:498px;height:1px;background:rgba(255,255,255,.6)}
.copy{left:0;top:1176px;width:797px;text-align:center;color:var(--white);font-size:7.4px}
</style>
</head>
<body>
<div class="abs topbar"></div>

<header>
  <div class="abs brand"><span class="brand-dot"></span>Gaumenweg Reisen</div>
  <nav class="abs nav">
    <a class="active" href="#">Home</a><a href="#">Shop</a><a href="#">Menüpunkt</a><a href="#">Menüpunkt</a><a href="#">Kontakt</a>
  </nav>
  <svg class="abs search" width="20" height="20" viewBox="0 0 20 20" aria-label="Suche">
    <circle cx="12.5" cy="7.5" r="5" fill="none" stroke="#111" stroke-width="2"/>
    <line x1="9" y1="11" x2="2" y2="18" stroke="#111" stroke-width="3" stroke-linecap="round"/>
  </svg>
</header>

<section>
  <div class="abs hero" role="img" aria-label="Foto: Schloss mit Weinranken unter bewölktem Himmel"></div>
  <div class="abs hero-title">Produktseite eins</div>
  <div class="abs hero-sub">vielleicht ein Untertitel</div>
</section>

<section>
  <div class="abs feature" role="img" aria-label="Foto: Weinglas, Trauben und Walnüsse auf einem Tisch im Weingarten">
    <div class="abs feature-script">Lorem Ipsum</div>
    <div class="abs feature-text">Finden Sie Ihr Geschmackserlebnis<br>in der Steiermark!</div>
    <div class="abs feature-btn">Alle ansehen</div>
  </div>

  <div class="abs thumb t1" role="img" aria-label="Foto: Weintrauben am Rebstock vor Weinbergen"></div>
  <div class="abs thumb t2" role="img" aria-label="Foto: Hauptplatz in Graz mit Uhrturm"></div>
  <div class="abs thumb t3" role="img" aria-label="Foto: Bergsee mit Felswand"></div>

  <div class="abs dots">
    <svg class="abs" style="left:0;top:-1px" width="8" height="12" viewBox="0 0 8 12"><polyline points="7,1 2,6 7,11" fill="none" stroke="#111" stroke-width="1.3"/></svg>
    <span class="dot on" style="left:34px"></span>
    <span class="dot" style="left:75px"></span>
    <span class="dot" style="left:117px"></span>
    <span class="dot" style="left:158px"></span>
    <span class="dot" style="left:200px"></span>
    <span class="dot" style="left:241px"></span>
    <span class="dot" style="left:283px"></span>
    <span class="dot" style="left:324px"></span>
    <svg class="abs" style="left:358px;top:-1px" width="8" height="12" viewBox="0 0 8 12"><polyline points="1,1 6,6 1,11" fill="none" stroke="#111" stroke-width="1.3"/></svg>
  </div>

  <div class="abs price">ab 1.650,00 €</div>
  <div class="abs vat">inkl. MwSt.</div>
  <div class="abs wish">
    <svg width="12" height="11" viewBox="0 0 24 22"><path d="M12 21 C5 15 1 11 1 6.5 A5.5 5.5 0 0 1 12 4 A5.5 5.5 0 0 1 23 6.5 C23 11 19 15 12 21Z" fill="#555"/></svg>
    Zur Merkliste hinzufügen
  </div>

  <div class="abs field" style="left:361px">Wählen Sie Ihren Reisetermin
    <svg width="12" height="12" viewBox="0 0 12 12"><rect x="1" y="2" width="10" height="9" fill="none" stroke="#555" stroke-width="1.2"/><line x1="1" y1="4.5" x2="11" y2="4.5" stroke="#555"/><line x1="3.5" y1="0.5" x2="3.5" y2="3" stroke="#555" stroke-width="1.2"/><line x1="8.5" y1="0.5" x2="8.5" y2="3" stroke="#555" stroke-width="1.2"/><polyline points="3.5,7.5 5.3,9.2 8.5,6" fill="none" stroke="#555" stroke-width="1.1"/></svg>
  </div>
  <div class="abs field" style="left:485px">Personenanzahl
    <svg width="12" height="10" viewBox="0 0 12 10"><circle cx="6" cy="3" r="2" fill="#555"/><circle cx="2.5" cy="3.8" r="1.4" fill="#555"/><circle cx="9.5" cy="3.8" r="1.4" fill="#555"/><path d="M2.5 10 Q6 4 9.5 10Z" fill="#555"/><path d="M0 9 Q2.5 5.5 4 8Z" fill="#555"/><path d="M12 9 Q9.5 5.5 8 8Z" fill="#555"/></svg>
  </div>
  <div class="abs book">jetzt buchen</div>
</section>

<section>
  <h2 class="abs intro-title" style="font-weight:400">Gaumenweg-Reise Südsteiermark</h2>
  <div class="abs intro">
    <p>Lernen Sie Leoben, die Hauptstadt des Mirtler-Bieres kennen &nbsp;und erfahren Sie im Mirtleum die Geschichte dieses weltbekannten Gebräus.<br>
    Entdecken Sie Graz, die ab-wechslungsreiche Landeshauptstadt und Kulturhauptstadt 2003, mit ihren vielfältigen kulturellen Angeboten, den charmanten Gassen und atem-beraubenden Ausblicken.<br>
    Genießen Sie die südlichere Sonne und kosten Sie die ausgezeichneten Weine der Winzer in der Buschenschank.</p>
    <p>Während unser Exklusiv Transfer Sie zu den Sehenswürdigkeiten bringt, lüftet unser steirischer Reiseleiter für Sie die Geheimnisse seines Heimatlandes, des „grünen Herzens Österreichs“ und führt Sie in erstklassige Restaurants. Sie wohnen in ausgesuchten Hotels in zentraler Lage.</p>
  </div>
</section>

<section>
  <div class="abs banner" role="img" aria-label="Foto: dunkle Weintrauben am Rebstock"></div>
  <h2 class="abs banner-title">Erleben Sie die<br>gastronomische Vielfalt der Süd-Steiermark</h2>
  <p class="abs banner-sub">Sie suchen ein bestimmtes Gaumenerlebnis?<br>Dann helfen wir Ihnen gerne weiter.</p>
  <div class="abs banner-btn">Jetzt beraten lassen</div>
</section>

<div class="abs hills" role="img" aria-label="Illustration: Silhouette der steirischen Berglandschaft mit Stadt"></div>

<footer>
  <div class="abs footer"></div>
  <svg class="abs f-ico" style="left:151px;top:1086px" width="8" height="10" viewBox="0 0 8 10"><path d="M4 10 C1 6 0 4.5 0 3.5 A4 4 0 0 1 8 3.5 C8 4.5 7 6 4 10Z" fill="#fff"/><circle cx="4" cy="3.6" r="1.4" fill="#236340"/></svg>
  <div class="abs f-name">Gaumenweg Reisen</div>
  <div class="abs f-addr">Marlene Hofbauer<br>Lindenweg 12<br>D - 10117 Musterstadt</div>
  <svg class="abs" style="left:151px;top:1133px" width="9" height="9" viewBox="0 0 24 24"><path d="M6.6 10.8a15 15 0 0 0 6.6 6.6l2.2-2.2a1 1 0 0 1 1-.25 11.4 11.4 0 0 0 3.6.57 1 1 0 0 1 1 1V20a1 1 0 0 1-1 1A17 17 0 0 1 3 4a1 1 0 0 1 1-1h3.5a1 1 0 0 1 1 1c0 1.25.2 2.45.57 3.6a1 1 0 0 1-.25 1z" fill="#fff"/></svg>
  <div class="abs f-phone">Deutschland: +49 170 0000 123<br>Österreich: +43 681 0000 4567</div>
  <div class="abs f-col" style="left:306px"><h4>MENÜ</h4><ul><li>MENÜPUNKT</li><li>MENÜPUNKT</li><li>MENÜPUNKT</li><li>MENÜPUNKT</li></ul></div>
  <div class="abs f-col" style="left:399px"><h4>MENÜ</h4><ul><li>MENÜPUNKT</li><li>MENÜPUNKT</li><li>MENÜPUNKT</li><li>MENÜPUNKT</li></ul></div>
  <div class="abs f-rule"></div>
  <div class="abs copy">© 2017. Agentur Krautner</div>
  <div class="abs footer-bottom"></div>
</footer>
</body>
</html>
```